RV BIZ CARDS

Hi,

Is it possible to see a one sided version (with logo and info) as well as a two-sided version (front side w/logo and back side with info)?
How do we choose card stock and finish once we approve a design?

We would like the following info included:

Marcus Trell
Trell Vantage Media
4157 Merrow Crescent, Suite 200
Los Angeles, CA 90068
(323) 555-0192
marcus@trellvantagemedia.example

```html
<!DOCTYPE html>
<html lang="en">
<head>
<meta charset="utf-8">
<title>Trell Vantage Media – Business Cards</title>
<link rel="stylesheet" href="https://fonts.googleapis.com/css2?family=Jost:wght@300;400;600&display=swap">
<style>
  :root {
    --canvas-bg: #e9e7e4;
    --card-bg: #ffffff;
    --ink: #1c1c1c;
    --ink-soft: #3a3a3a;
    --accent: #5b1f1c;
    --rule: #222222;
    --card-shadow: rgba(0, 0, 0, 0.12);
  }
  * { box-sizing: border-box; margin: 0; padding: 0; }
  html, body {
    width: 1200px;
    height: 873px;
    overflow: hidden;
    background: var(--canvas-bg);
    font-family: "Jost", "Futura", sans-serif;
    color: var(--ink);
  }
  .sheet {
    width: 1200px;
    height: 873px;
    display: flex;
    align-items: center;
    justify-content: center;
    gap: 40px;
  }
  .card {
    width: 540px;
    height: 309px;
    background: var(--card-bg);
    box-shadow: 0 2px 10px var(--card-shadow);
    position: relative;
  }

  /* brand lockup */
  .brand {
    display: flex;
    flex-direction: column;
    align-items: center;
  }
  .brand-dot {
    border: 2px solid var(--accent);
    border-radius: 50%;
  }
  .brand-name {
    font-weight: 300;
    text-transform: uppercase;
    color: var(--ink);
    white-space: nowrap;
  }

  /* back: info side */
  .card-back {
    display: flex;
    align-items: center;
  }
  .card-back .brand {
    width: 50%;
    gap: 10px;
  }
  .card-back .brand-dot { width: 30px; height: 30px; }
  .card-back .brand-name { font-size: 17px; letter-spacing: 2.5px; }
  .divider {
    width: 1.5px;
    height: 120px;
    background: var(--rule);
  }
  .contact {
    padding-left: 26px;
    width: calc(50% - 2px);
  }
  .contact-name {
    font-weight: 600;
    font-size: 17px;
    line-height: 1.1;
  }
  .contact-company {
    font-weight: 300;
    font-size: 15px;
    margin-bottom: 10px;
  }
  .contact-list { list-style: none; }
  .contact-item {
    display: flex;
    align-items: flex-start;
    gap: 7px;
    font-size: 10.5px;
    font-weight: 400;
    color: var(--ink-soft);
    line-height: 1.45;
  }
  .contact-icon {
    width: 9px;
    height: 9px;
    margin-top: 3px;
    flex-shrink: 0;
  }

  /* front: logo side */
  .card-front {
    display: flex;
    align-items: center;
    justify-content: center;
  }
  .card-front .brand { gap: 14px; }
  .card-front .brand-dot { width: 46px; height: 46px; }
  .card-front .brand-name { font-size: 27px; letter-spacing: 4px; }
</style>
</head>
<body>
<main class="sheet">

  <section class="card card-back" aria-label="Card back with contact details">
    <div class="brand">
      <span class="brand-dot" aria-hidden="true"></span>
      <span class="brand-name">Trell Vantage</span>
    </div>
    <span class="divider" aria-hidden="true"></span>
    <div class="contact">
      <p class="contact-name">Marcus Trell</p>
      <p class="contact-company">Trell Vantage Media</p>
      <ul class="contact-list">
        <li class="contact-item">
          <svg class="contact-icon" viewBox="0 0 10 10" aria-hidden="true"><path d="M1 5 L5 1.5 L9 5 M2.3 4 V9 H7.7 V4" fill="none" stroke="currentColor" stroke-width="1"/></svg>
          <span>4157 Merrow Crescent, Suite 200<br>Los Angeles, CA 90068</span>
        </li>
        <li class="contact-item">
          <svg class="contact-icon" viewBox="0 0 10 10" aria-hidden="true"><path d="M2.5 1 L4 3 L3 4.2 Q4.3 6.3 5.8 7 L7 6 L9 7.5 L8 9 Q3.5 8.5 1 2 Z" fill="none" stroke="currentColor" stroke-width="0.9"/></svg>
          <span>(323) 555-0192</span>
        </li>
        <li class="contact-item">
          <svg class="contact-icon" viewBox="0 0 10 10" aria-hidden="true"><rect x="1" y="2.2" width="8" height="5.6" fill="none" stroke="currentColor" stroke-width="0.9"/><path d="M1 2.4 L5 5.4 L9 2.4" fill="none" stroke="currentColor" stroke-width="0.9"/></svg>
          <span>marcus@trellvantagemedia.example</span>
        </li>
      </ul>
    </div>
  </section>

  <section class="card card-front" aria-label="Card front with brand name">
    <div class="brand">
      <span class="brand-dot" aria-hidden="true"></span>
      <span class="brand-name">Trell Vantage</span>
    </div>
  </section>

</main>
</body>
</html>
```